Real Estate For Sale Signage

I'm an independent agent in Lismore NSW Australia with high standards and looking for a catching 'For Sale'sign board.
I like classy, elegant, stylish and simple best.
My colours are red, white and black.
I don't have a logo or other font designs I need to stick to. I like the concept of a house or real estate design.
Before I created this project I played around on publisher and created the PDF attached. I'm not sold on it, but I don't mind the way the name has been layed out. Originally I had a white background with black & red font.
Fancy fonts for my name would be nice, but must not be busy.
Updates

Just wanted to advise that I have updated my brief and used the tools available to help get my ideas through.

Thank you for your work and time.

Kind regards
Marella

Industry/Entity Type

Real Estate

Requirements
Must have
• For Sale
Marella Quint Real Estate (must stand out)
0400 517 382 (must stand out)
17 Tallowood Street North Lismore
www.marellaquintrealestate.com.au

```html
<!DOCTYPE html>
<html lang="en">
<head>
<meta charset="utf-8">
<title>For Sale – Marella Quint Real Estate</title>
<link rel="stylesheet" href="https://fonts.googleapis.com/css2?family=Cinzel:wght@600;700;800&display=swap">
<style>
  :root {
    --red-core: #e0141a;
    --red-mid: #b8070c;
    --red-edge: #6e0204;
    --frame: #3a3a3a;
    --silver-hi: #ffffff;
    --silver-mid: #c9c9cc;
    --silver-lo: #8d8d92;
    --gold-hi: #fff2b0;
    --gold: #e2b93b;
    --gold-lo: #9a6d12;
    --blush: #f3d9d9;
  }
  html, body {
    margin: 0;
    padding: 0;
    width: 1200px;
    height: 849px;
    overflow: hidden;
    background: #ffffff;
  }
  .sign {
    position: relative;
    width: 1200px;
    height: 849px;
    box-sizing: border-box;
    border: 3px solid var(--frame);
    background: radial-gradient(ellipse 62% 62% at 50% 46%, var(--red-core) 0%, var(--red-mid) 55%, var(--red-edge) 100%);
    overflow: hidden;
  }
  .sign__art {
    position: absolute;
    inset: 0;
    width: 100%;
    height: 100%;
  }
  .headline, .agency, .phone, .address, .website {
    font-family: "Cinzel", "Trajan Pro", serif;
  }
  .headline {
    font-weight: 700;
    fill: url(#silver);
    stroke: url(#gold);
    paint-order: stroke fill;
    stroke-linejoin: round;
  }
  .headline--for { font-size: 116px; stroke-width: 7px; }
  .headline--sale { font-size: 300px; stroke-width: 12px; }
  .agency {
    font-weight: 700;
    font-size: 66px;
    fill: url(#gold);
    stroke: #5a1a00;
    stroke-width: 1.2px;
    paint-order: stroke fill;
  }
  .phone {
    font-weight: 700;
    font-size: 186px;
    fill: url(#silver);
    stroke: url(#gold);
    stroke-width: 12px;
    paint-order: stroke fill;
    stroke-linejoin: round;
  }
  .address {
    font-weight: 700;
    font-size: 40px;
    fill: var(--blush);
  }
  .website {
    font-weight: 600;
    font-size: 27px;
    fill: var(--blush);
  }
</style>
</head>
<body>
  <main class="sign">
    <svg class="sign__art" viewBox="0 0 1194 843" xmlns="http://www.w3.org/2000/svg" aria-label="For Sale – Marella Quint Real Estate – 0400 517 382">
      <defs>
        <linearGradient id="silver" x1="0" y1="0" x2="0" y2="1">
          <stop offset="0" stop-color="var(--silver-hi)"/>
          <stop offset="0.45" stop-color="var(--silver-mid)"/>
          <stop offset="0.55" stop-color="var(--silver-lo)"/>
          <stop offset="1" stop-color="var(--silver-hi)"/>
        </linearGradient>
        <linearGradient id="gold" x1="0" y1="0" x2="0" y2="1">
          <stop offset="0" stop-color="var(--gold-hi)"/>
          <stop offset="0.5" stop-color="var(--gold)"/>
          <stop offset="1" stop-color="var(--gold-lo)"/>
        </linearGradient>
        <filter id="lift" x="-10%" y="-10%" width="120%" height="130%">
          <feDropShadow dx="0" dy="4" stdDeviation="4" flood-color="#2a0000" flood-opacity="0.7"/>
        </filter>
      </defs>

      <g filter="url(#lift)">
        <text class="headline headline--for" x="597" y="143" text-anchor="middle" textLength="330" lengthAdjust="spacingAndGlyphs">FOR</text>
        <text class="headline headline--sale" x="597" y="380" text-anchor="middle" textLength="600" lengthAdjust="spacingAndGlyphs">SALE</text>

        <text class="agency" x="597" y="480" text-anchor="middle" textLength="626" lengthAdjust="spacingAndGlyphs">MARELLA QUINT</text>
        <text class="agency" x="597" y="549" text-anchor="middle" textLength="452" lengthAdjust="spacingAndGlyphs">REAL ESTATE</text>

        <text class="phone" x="630" y="703" text-anchor="middle" textLength="935" lengthAdjust="spacingAndGlyphs">0400 517 382</text>
      </g>

      <text class="address" x="597" y="766" text-anchor="middle" textLength="900" lengthAdjust="spacingAndGlyphs">17 Tallowood Street North Lismore</text>
      <text class="website" x="597" y="801" text-anchor="middle" textLength="780" lengthAdjust="spacingAndGlyphs">www.marellaquintrealestate.com.au</text>
    </svg>
  </main>
</body>
</html>
```